Established food business needs a new name card design

Refer to attached current name card. Would like a new professional look design with only the company name and logo without any pictures. Would like green and yellow to be included.
To include:
My name "IBRAHIM SUKRI" and hand phone number "87260413".
To delete "
"Along Brackendale Ave 8" and
"www.nur-tiwas.com.sg"
To change email to:
"tkr27@velmorix.com.sg"

```html
<!DOCTYPE html>
<html lang="en">
<head>
<meta charset="utf-8">
<title>Nur-Tiwas Eating Corner — Name Card</title>
<link rel="stylesheet" href="https://fonts.googleapis.com/css2?family=Archivo+Black&family=Josefin+Sans:wght@400;600&display=swap">
<style>
  :root {
    --stage: #2b2c2e;
    --green-deep: #01160f;
    --green-dark: #033a26;
    --green-mid: #06704a;
    --gold: #f2d64a;
    --gold-light: #fff2a0;
    --gold-dark: #b8891c;
  }
  * { box-sizing: border-box; margin: 0; padding: 0; }
  html, body { width: 1200px; height: 900px; overflow: hidden; }
  body {
    background: var(--stage);
    display: flex;
    flex-direction: column;
    align-items: center;
    justify-content: center;
    gap: 40px;
    font-family: "Josefin Sans", sans-serif;
  }
  .card {
    position: relative;
    width: 700px;
    height: 400px;
    border-radius: 26px;
    overflow: hidden;
  }
  .card--front {
    background: radial-gradient(ellipse at 40% 25%, var(--green-mid) 0%, var(--green-dark) 45%, var(--green-deep) 100%);
  }
  .card--back {
    background: radial-gradient(ellipse at 55% 50%, var(--green-mid) 0%, var(--green-dark) 70%, var(--green-deep) 110%);
  }
  .ornament {
    position: absolute;
    border-radius: 50%;
    background: radial-gradient(ellipse at center, rgba(255,242,160,.55) 0%, rgba(214,170,40,.35) 45%, rgba(184,137,28,0) 72%);
  }
  .card--front .ornament { left: 130px; top: -60px; width: 420px; height: 230px; }
  .card--back .ornament { right: -40px; top: -10px; width: 420px; height: 420px; }

  .brand {
    position: absolute;
    left: 0; right: 0; top: 205px;
    display: flex;
    flex-direction: column;
    align-items: center;
  }
  .brand__row { display: flex; align-items: center; gap: 14px; }
  .brand__dot {
    width: 18px; height: 18px; border-radius: 50%;
    background: var(--gold);
  }
  .brand__name {
    font-weight: 600;
    font-size: 46px;
    letter-spacing: 3px;
    color: var(--gold);
    line-height: 1;
  }
  .brand__rule {
    width: 300px; height: 2px; margin: 10px 0 8px;
    background: var(--gold);
  }
  .brand__tagline {
    font-weight: 400;
    font-size: 17px;
    letter-spacing: 6px;
    color: var(--gold-dark);
  }

  .holder {
    position: absolute;
    left: 50px; top: 70px;
    font-family: "Archivo Black", sans-serif;
    font-size: 40px;
    letter-spacing: 2px;
    color: var(--gold);
  }
  .contacts {
    position: absolute;
    left: 70px; top: 230px;
    list-style: none;
    display: flex;
    flex-direction: column;
    gap: 22px;
  }
  .contacts__item {
    display: flex; align-items: center; gap: 16px;
    font-size: 19px; letter-spacing: 2px;
    color: var(--gold);
    text-transform: uppercase;
  }
  .contacts__icon { width: 22px; height: 22px; fill: var(--gold); }
</style>
</head>
<body>

  <section class="card card--front" aria-label="Card front">
    <div class="ornament" role="img" aria-label="Gold floral scroll ornament"></div>
    <div class="brand">
      <div class="brand__row">
        <span class="brand__dot"></span>
        <span class="brand__name">NUR-TIWAS</span>
      </div>
      <div class="brand__rule"></div>
      <div class="brand__tagline">EATING CORNER</div>
    </div>
  </section>

  <section class="card card--back" aria-label="Card back">
    <div class="ornament" role="img" aria-label="Large gold floral scroll ornament"></div>
    <h1 class="holder">IBRAHIM SUKRI</h1>
    <ul class="contacts">
      <li class="contacts__item">
        <svg class="contacts__icon" viewBox="0 0 24 24"><path d="M6.6 10.8a15.1 15.1 0 0 0 6.6 6.6l2.2-2.2c.3-.3.7-.4 1-.2 1.1.4 2.3.6 3.6.6.6 0 1 .4 1 1V20c0 .6-.4 1-1 1A17 17 0 0 1 3 4c0-.6.4-1 1-1h3.5c.6 0 1 .4 1 1 0 1.3.2 2.5.6 3.6.1.3 0 .7-.2 1z"/></svg>
        87260413
      </li>
      <li class="contacts__item">
        <svg class="contacts__icon" viewBox="0 0 24 24"><path d="M2 5h20v14H2zm2 2v.5l8 5 8-5V7zm0 2.8V17h16V9.8l-8 5z"/></svg>
        tkr27@velmorix.com.sg
      </li>
    </ul>
  </section>

</body>
</html>
```